We sell companies excess stock for them

We need a business card for a company based in New Zealand called 'StockHarbor'.

Check out our website to get an idea www.stockharbor.example

We help other businesses to;
- Sell Excess Stock
- Manage Product Returns
- Sell Company Assets

Our logo is attached for your reference
The font used is 'RifficFree-Bold'

Target Market(s)

Businesses

Industry/Entity Type

Business

Contact Information for Business Card

Name: Mark Pellow
Phone: 027 846 2093
email: markpellow@stockharbor.example
website: www.stockharbor.example

Font styles to use
Other font styles liked:
• Unsure

Colors
9bcb3b

Requirements
Must have
• coming soon
Nice to have
• coming soon
Should not have
• coming soon

```html
<!DOCTYPE html>
<html lang="en">
<head>
<meta charset="utf-8">
<title>StockHarbor Business Card</title>
<link href="https://fonts.googleapis.com/css2?family=Fredoka:wght@700&family=Lato:wght@400&display=swap" rel="stylesheet">
<style>
  :root {
    --brand-green: #9bcb3b;
    --ink: #2b2828;
    --paper: #ffffff;
    --backdrop: #e9e9e6;
    --mascot-orange: #f29a2e;
    --mascot-green: #7fb52b;
  }
  * { box-sizing: border-box; margin: 0; padding: 0; }
  html, body { width: 1189px; height: 1200px; overflow: hidden; }
  body {
    background: var(--backdrop);
    position: relative;
    font-family: "Lato", sans-serif;
  }
  .card {
    position: absolute;
    left: 166px;
    width: 857px;
    height: 490px;
    border-radius: 26px;
    overflow: hidden;
    box-shadow: 0 6px 18px rgba(0,0,0,0.18);
  }
  .card--front { top: 66px; background: var(--brand-green); }
  .card--back { top: 625px; background: var(--paper); }

  .mascot-art {
    position: absolute;
    border-radius: 40%;
    background: radial-gradient(circle at 45% 40%, var(--mascot-orange) 0%, var(--mascot-green) 55%, rgba(127,181,43,0) 72%);
  }
  .card--front .mascot-art { left: 266px; top: 73px; width: 322px; height: 342px; }
  .card--back .mascot-art { left: 89px; top: 119px; width: 238px; height: 251px; }

  .footer-band {
    position: absolute;
    left: 0; right: 0; bottom: 0;
    background: var(--ink);
  }
  .card--front .footer-band { top: 435px; border-top: 4px solid var(--paper); }
  .card--back .footer-band { top: 398px; border-top: 5px solid var(--brand-green); }

  .front-url {
    position: absolute;
    left: 0; right: 0; top: 446px;
    text-align: center;
    color: var(--brand-green);
    font-size: 18px;
    letter-spacing: 4.5px;
  }

  .divider {
    position: absolute;
    left: 397px; top: 118px;
    width: 2px; height: 252px;
    background: var(--brand-green);
  }
  .company-name {
    position: absolute;
    left: 462px; top: 114px;
    font-family: "Fredoka", sans-serif;
    font-weight: 700;
    font-size: 48px;
    letter-spacing: -1.5px;
    color: var(--ink);
  }
  .person-name {
    position: absolute;
    left: 463px; top: 220px;
    font-family: "Fredoka", sans-serif;
    font-weight: 700;
    font-size: 33px;
    letter-spacing: -0.5px;
    color: var(--ink);
  }
  .person-name .surname { color: var(--brand-green); }

  .contact-list {
    position: absolute;
    left: 467px; top: 272px;
    list-style: none;
  }
  .contact-list li {
    display: flex;
    align-items: center;
    height: 29px;
    font-size: 21px;
    color: var(--ink);
  }
  .contact-list svg { width: 25px; height: 25px; margin-right: 8px; flex: none; }

  .tagline {
    position: absolute;
    left: 0; right: 0; top: 404px;
    text-align: center;
  }
  .tagline-lead {
    font-family: "Fredoka", sans-serif;
    font-weight: 700;
    font-size: 31px;
    color: var(--brand-green);
    line-height: 36px;
  }
  .tagline-services {
    font-size: 20px;
    color: var(--paper);
    line-height: 24px;
  }
</style>
</head>
<body>

<section class="card card--front">
  <div class="mascot-art" role="img" aria-label="Mascot illustration: smiling courier in green cap and overalls running with an orange parcel, giving a thumbs up"></div>
  <div class="footer-band"></div>
  <p class="front-url">www.stockharbor.example</p>
</section>

<section class="card card--back">
  <div class="mascot-art" role="img" aria-label="Mascot illustration: smiling courier in green cap and overalls running with an orange parcel, giving a thumbs up"></div>
  <div class="divider"></div>

  <h1 class="company-name">StockHarbor</h1>
  <h2 class="person-name">Mark <span class="surname">Pellow</span></h2>

  <ul class="contact-list">
    <li>
      <svg viewBox="0 0 25 25" aria-hidden="true">
        <circle cx="12.5" cy="12.5" r="11" fill="none" stroke="#9bcb3b" stroke-width="1.6"/>
        <path d="M9 7.5c-1 .5-1.5 1.5-1 3 1 3 3 5.5 6 7 1.2.5 2.2 0 2.8-.8l-1.8-1.8-1.4.8c-1.3-.8-2.5-2.2-3.2-3.6l.9-1.3z" fill="none" stroke="#9bcb3b" stroke-width="1.4" stroke-linejoin="round"/>
      </svg>
      027 846 2093
    </li>
    <li>
      <svg viewBox="0 0 25 25" aria-hidden="true">
        <circle cx="12.5" cy="12.5" r="11" fill="none" stroke="#9bcb3b" stroke-width="1.6"/>
        <rect x="6.5" y="8.5" width="12" height="8.5" fill="#9bcb3b"/>
        <path d="M6.5 8.5l6 5 6-5" fill="none" stroke="#fff" stroke-width="1.2"/>
      </svg>
      markpellow@stockharbor.example
    </li>
    <li>
      <svg viewBox="0 0 25 25" aria-hidden="true">
        <circle cx="12.5" cy="12.5" r="11" fill="none" stroke="#9bcb3b" stroke-width="1.6"/>
        <circle cx="12.5" cy="12.5" r="7" fill="#9bcb3b"/>
        <path d="M5.5 12.5h14M12.5 5.5v14M12.5 5.5c-3 3.5-3 10.5 0 14M12.5 5.5c3 3.5 3 10.5 0 14" fill="none" stroke="#fff" stroke-width="0.9"/>
      </svg>
      www.stockharbor.example
    </li>
  </ul>

  <div class="footer-band"></div>
  <div class="tagline">
    <p class="tagline-lead">We help other businesses to</p>
    <p class="tagline-services">Sell Excess Stock | Manage Product Returns | Sell Company Assets</p>
  </div>
</section>

</body>
</html>
```